New Wine Label - Argentinian Malbec 'Brisa Dorada'

I am looking for an exceptional and exciting design for a wine label called 'Brisa Dorada' meaning Golden Breeze or Breeze of Gold. The design must feature the name 'Brisa Dorada', a star logo and the word 'Malbec'. It will also need the words 'Mendoza, Argentina' at the bottom of the label as a prominent piece of information. Please produce the work in size 80mm x 100mm. Feel free to use colour in addition to black/white and ensue that the label is easy to read on a shelf placement.

Target Market(s)

25-50 Year Olds who enjoy great wine that looks and appears interesting and a little different.

Requirements
Must have
• Star Logo
• Word - Malbec
• Words - Mendoza, Argentina
Nice to have
• Background image to label

```html
<!DOCTYPE html>
<html lang="en">
<head>
<meta charset="utf-8">
<title>Brisa Dorada Malbec Label</title>
<link rel="stylesheet" href="https://fonts.googleapis.com/css2?family=Barlow+Condensed:wght@500;600&family=Libre+Baskerville:ital@1&display=swap">
<style>
  :root {
    --backdrop: #ebebeb;
    --label: #f1eff0;
    --ink: #231f1e;
    --gold: #c9a24e;
    --wine: #a3273a;
    --rule: #cfc9c7;
  }
  html, body {
    margin: 0;
    padding: 0;
    width: 1200px;
    height: 1200px;
    overflow: hidden;
    background: var(--backdrop);
  }
  .label {
    position: absolute;
    left: 190px;
    top: 207px;
    width: 820px;
    height: 785px;
    background: var(--label);
    border-radius: 3px;
  }
  .star-mark {
    position: absolute;
    left: 396px;
    top: 238px;
    width: 24px;
    height: 24px;
    border-radius: 50%;
    background: var(--gold);
  }
  .wordmark {
    position: absolute;
    left: 0;
    top: 395px;
    width: 100%;
    margin: 0;
    text-align: center;
    font-family: "Barlow Condensed", sans-serif;
    font-weight: 600;
    font-size: 80px;
    line-height: 75px;
    letter-spacing: 1px;
    color: var(--ink);
    text-transform: uppercase;
  }
  .details {
    position: absolute;
    left: 0;
    top: 585px;
    width: 100%;
    height: 90px;
  }
  .details__divider {
    position: absolute;
    left: 444px;
    top: 0;
    width: 1px;
    height: 88px;
    background: var(--rule);
  }
  .wine-info {
    position: absolute;
    right: 386px;
    top: 0;
    text-align: right;
  }
  .wine-info__variety {
    font-family: "Barlow Condensed", sans-serif;
    font-weight: 600;
    font-size: 27px;
    letter-spacing: 2px;
    color: var(--ink);
    line-height: 30px;
  }
  .wine-info__origin {
    font-family: "Libre Baskerville", serif;
    font-style: italic;
    font-size: 17px;
    color: var(--ink);
    line-height: 28px;
  }
  .wine-info__vintage {
    font-family: "Barlow Condensed", sans-serif;
    font-weight: 600;
    font-size: 19px;
    letter-spacing: 3px;
    color: var(--ink);
    line-height: 26px;
  }
  .wine-info__vintage span { color: var(--wine); }
  .winemaker {
    position: absolute;
    left: 438px;
    top: 0;
  }
  .winemaker__signature {
    display: block;
    width: 160px;
    height: 30px;
    margin-top: 4px;
    background: linear-gradient(90deg, rgba(201,162,78,0.15), rgba(201,162,78,0.55), rgba(201,162,78,0.15));
    border-radius: 15px;
  }
  .winemaker__title {
    margin-left: 24px;
    font-family: "Libre Baskerville", serif;
    font-style: italic;
    font-size: 17px;
    line-height: 26px;
    color: var(--ink);
  }
</style>
</head>
<body>
  <main class="label">
    <div class="star-mark" aria-hidden="true"></div>
    <h1 class="wordmark">Brisa<br>Dorada</h1>
    <section class="details">
      <div class="wine-info">
        <div class="wine-info__variety">Malbec</div>
        <div class="wine-info__origin">Mendoza, Argentina</div>
        <div class="wine-info__vintage">20<span>12</span></div>
      </div>
      <div class="details__divider"></div>
      <div class="winemaker">
        <span class="winemaker__signature" role="img" aria-label="Winemaker's handwritten signature in gold"></span>
        <div class="winemaker__title">Winemaker</div>
      </div>
    </section>
  </main>
</body>
</html>
```